Q R Ventral Harbor Works, LLC
I just posted pic to use....
where we can find the details for this project....can u upload it in pdf format...so we can start designing it..
Sorry looking for a Trifold brochure

```html
<!DOCTYPE html>
<html lang="en">
<head>
<meta charset="utf-8">
<title>Q R Ventral Harbor Works — Trifold Brochure</title>
<link href="https://fonts.googleapis.com/css2?family=EB+Garamond:wght@400;600;700&display=swap" rel="stylesheet">
<style>
:root{
  --stage:#e9e6e2;
  --ink:#121212;
  --ink-soft:#1c1c1c;
  --navy:#0c1a33;
  --navy-deep:#081226;
  --blue:#1d4f8c;
  --orange:#e8731a;
  --orange-deep:#b8520c;
  --paper:#ffffff;
  --grey:#d9dde2;
  --text-light:#e6e6e6;
}
*{box-sizing:border-box;margin:0;padding:0}
html,body{width:1200px;height:545px;overflow:hidden;background:var(--stage)}
body{font-family:"EB Garamond",Georgia,serif;position:relative}
.sheet{position:absolute;top:38px;width:575px;height:470px;display:flex;box-shadow:0 3px 10px rgba(0,0,0,.35)}
.sheet--outside{left:15px}
.sheet--inside{left:610px}
.panel{width:191.66px;height:100%;position:relative;overflow:hidden;color:var(--text-light);font-size:6.4px;line-height:1.35}
.panel+.panel{border-left:1px solid rgba(255,255,255,.08)}
.panel p{margin-bottom:5px}
.dark{background:linear-gradient(180deg,var(--ink) 0%,var(--ink-soft) 60%,var(--navy) 100%)}
.dark-navy{background:linear-gradient(180deg,#0e0e0e 0%,#101a2b 55%,var(--navy-deep) 100%)}
.pad{padding:8px 11px}
.photo{display:block;width:100%}
.tab{display:inline-block;background:linear-gradient(90deg,var(--orange),var(--orange-deep));color:#fff;font-weight:700;font-size:8px;letter-spacing:.4px;padding:2px 10px 2px 8px;margin:0 0 6px -11px;border-radius:0 8px 8px 0;text-transform:uppercase}
.sub{color:var(--orange);font-weight:700;font-size:8.5px;margin:6px 0 3px}
.bullets{list-style:none;margin-bottom:6px}
.bullets li{padding-left:8px;position:relative;margin-bottom:2px}
.bullets li::before{content:"";position:absolute;left:0;top:2.5px;width:3px;height:3px;background:var(--orange)}
.cover{background:var(--paper);color:var(--ink)}
.brand{display:flex;align-items:center;gap:6px;padding:18px 12px 10px}
.brand-mark{width:14px;height:14px;background:var(--orange);flex:none}
.brand-name{font-weight:700;font-size:10.5px;color:var(--blue);line-height:1.1}
.cover-title{background:linear-gradient(180deg,#f3f3f3,var(--grey));border-top:3px solid var(--orange);border-bottom:3px solid var(--orange);text-align:center;padding:9px 6px;font-weight:700;color:var(--navy);text-transform:uppercase;font-size:12px;line-height:1.15}
.cover-title small{display:block;font-size:7.5px;color:var(--orange-deep);margin-top:3px;letter-spacing:.5px}
.cover-base{position:absolute;left:0;right:0;bottom:0;height:110px;background:linear-gradient(180deg,var(--ink),var(--navy));text-align:center;padding-top:34px}
.phone{color:var(--orange);font-size:22px;font-weight:600;letter-spacing:.5px}
.web{color:#fff;font-size:8px;margin-top:4px}
.service{display:flex;gap:6px;margin-bottom:6px}
.service .thumb{width:48px;height:40px;flex:none;border:1px solid var(--orange)}
.service h4{color:var(--orange);font-size:7.8px;margin-bottom:1px}
.footer-web{position:absolute;bottom:10px;right:11px;color:var(--orange);font-size:7.5px}
.contact{position:absolute;left:11px;right:11px;bottom:12px}
</style>
</head>
<body>

<section class="sheet sheet--outside">
  <div class="panel dark">
    <svg class="photo" width="192" height="120" role="img" aria-label="Illustration of colourful business figures climbing a ladder">
      <defs><linearGradient id="g1" x1="0" y1="0" x2="0" y2="1"><stop offset="0" stop-color="#f4f4f4"/><stop offset="1" stop-color="#c9d3de"/></linearGradient></defs>
      <rect width="192" height="120" fill="url(#g1)"/>
    </svg>
    <div class="pad">
      <div class="sub" style="margin-top:2px">Q R Ventral Harbor Works, LLC</div>
      <p>Q R Ventral Harbor Works, LLC is a human resources consulting firm that helps growing organizations plan, staff and manage their people. We pair seasoned advisers with practical tools so every client can build a stronger, more confident workforce.</p>
      <p>Our specialists listen first, then shape programs around your goals, your budget and your culture. From a single policy review to a complete outsourced department, we deliver steady support that keeps teams compliant, engaged and ready for what comes next.</p>
      <p>We measure success by the results our partners see: lower turnover, clearer processes and people who know where they are headed.</p>
      <p>Whatever the size of your organization, our team stays close from the first meeting to the final report.</p>
    </div>
  </div>

  <div class="panel dark">
    <div class="pad">
      <div class="tab">About Us</div>
      <p>Founded to serve public and private employers, our team brings decades of combined experience in workforce planning, training and employee relations. We believe good HR is simple, honest and built to last.</p>
      <ul class="bullets">
        <li>Strategic human resources planning</li>
        <li>Leadership development and coaching programs</li>
        <li>Recruitment and retention support</li>
        <li>Policy, handbook and compliance reviews</li>
        <li>Payroll and benefits administration</li>
        <li>Training design and delivery for every level</li>
      </ul>
      <p>Each engagement is led by a senior adviser who knows your goals and answers for the outcome.</p>
    </div>
    <div class="contact">
      <div class="tab">Contact Us</div>
      <p>1200 Harbor Point Road, Suite 40<br>Baltimore, MD 21230<br>Phone: 301-555-0147<br>info@qrventralharbor.com</p>
    </div>
  </div>

  <div class="panel cover">
    <div class="brand"><span class="brand-mark"></span><span class="brand-name">Q R Ventral Harbor Works</span></div>
    <div class="cover-title">Complete and<br>Sustainable HR<small>Solutions from A to Z</small></div>
    <svg class="photo" width="192" height="140" role="img" aria-label="Photo of a smiling business team gathered around a laptop">
      <defs><linearGradient id="g2" x1="0" y1="0" x2="1" y2="1"><stop offset="0" stop-color="#eef1f4"/><stop offset="1" stop-color="#b9c2cc"/></linearGradient></defs>
      <rect width="192" height="140" fill="url(#g2)"/>
    </svg>
    <div class="cover-base">
      <div class="phone">301-555-0147</div>
      <div class="web">qrventralharbor.com</div>
    </div>
  </div>
</section>

<section class="sheet sheet--inside">
  <div class="panel dark-navy">
    <div class="pad">
      <div class="tab">Our Solutions and Philosophy</div>
      <p>We believe that people are the engine of every organization. Our solutions begin with a clear understanding of your mission and grow into programs that support managers, reward employees and protect the business from avoidable risk.</p>
      <div class="sub">Solutions That Save Growth</div>
      <p>Growth brings new hires, new rules and new pressure on leaders. We help you scale with confidence by building hiring plans, onboarding steps and performance tools that keep pace with your ambitions without adding needless cost.</p>
      <p>Our advisers stay involved after launch, checking results and adjusting programs as your needs change.</p>
      <div class="sub">What Distinguishes Q R Ventral Harbor Works</div>
      <p>We combine the reach of a full service firm with the attention of a small partner. Every client has direct access to senior staff, plain answers and reporting that shows exactly where progress has been made.</p>
    </div>
  </div>

  <div class="panel dark-navy">
    <div class="pad">
      <div class="tab">Our Services</div>
      <p>We offer a complete range of HR services, delivered as single projects or ongoing support.</p>
      <div class="service">
        <svg class="thumb" role="img" aria-label="Photo of a planning meeting"><rect width="48" height="40" fill="#8c9bb0"/></svg>
        <div><h4>Planning and Management</h4><p>Workforce forecasts, job structures and clear plans for future staffing needs.</p></div>
      </div>
      <div class="service">
        <svg class="thumb" role="img" aria-label="Photo of a manager at a desk"><rect width="48" height="40" fill="#9a8d80"/></svg>
        <div><h4>Program Management</h4><p>Oversight of training, benefits and wellness programs from design to review.</p></div>
      </div>
      <div class="service">
        <svg class="thumb" role="img" aria-label="Photo of documents and a calculator"><rect width="48" height="40" fill="#7f8f9c"/></svg>
        <div><h4>Compliance and Logistic Management</h4><p>Audits, records and policies that keep you aligned with current regulations.</p></div>
      </div>
      <div class="service">
        <svg class="thumb" role="img" aria-label="Photo of a person working on a computer"><rect width="48" height="40" fill="#6f8aa8"/></svg>
        <div><h4>Information Technology</h4><p>HR systems setup, data reporting and secure employee self service tools.</p></div>
      </div>
    </div>
  </div>

  <div class="panel dark-navy">
    <svg class="photo" width="192" height="92" role="img" aria-label="Photo of a business professional shaking hands">
      <defs><linearGradient id="g3" x1="0" y1="0" x2="1" y2="0"><stop offset="0" stop-color="#5c6f86"/><stop offset="1" stop-color="#c4ccd5"/></linearGradient></defs>
      <rect width="192" height="92" fill="url(#g3)"/>
    </svg>
    <div class="pad">
      <div class="tab">Strategic Capital Outsourcing</div>
      <p>Outsourcing HR lets your leaders focus on the work that matters most. We can run daily HR operations on your behalf, providing trained staff, proven processes and reliable reporting at a predictable monthly cost.</p>
      <div class="sub">Staffing Services</div>
      <ul class="bullets">
        <li>Temporary staffing</li>
        <li>Direct hire placement</li>
        <li>Executive search</li>
        <li>Contract to hire</li>
        <li>Background screening</li>
        <li>Onboarding support</li>
        <li>Exit interviews</li>
      </ul>
    </div>
    <div class="footer-web">qrventralharbor.com</div>
  </div>
</section>

</body>
</html>
```